New Business Card Design Project

I would like to purchase a customized version of a design you have previously submitted - https://www.plomarket.com/design/7724163<br/><br/>I would like to incorporate the attached Images for my fitness company "TalvrenPro Athletics". My initial services is personal training and athletic performance. I would like a card that has one a shiny black side with the silver logo and the side with a white background utilizing the gold logo. On the white side, put "Sports Performance and Functional Strength Training" under the logo.
Industry/Entity Type
Fitness
Contact Information for Business Card
Marcus Tolley
Owner and Trainer
555.273.8492
marcus.tolley@talvrenproathletics.com
Look and feel
Each slider illustrates characteristics of the customer's brand and the style your logo design should communicate.

```html
<!DOCTYPE html>
<html lang="en">
<head>
<meta charset="utf-8">
<title>TalvrenPro Athletics – Business Card</title>
<link rel="stylesheet" href="https://fonts.googleapis.com/css2?family=Lato:wght@400;700&display=swap">
<style>
  :root {
    --backdrop: #3a322d;
    --card-black: #0d0d0d;
    --card-white: #f7f6f3;
    --silver: #c9c9c9;
    --gold: #b8913f;
    --ink-dim: #4a4a4a;
    --ink-mid: #5a5a5a;
    --ink-dark: #3a3a3a;
  }
  html, body {
    margin: 0;
    padding: 0;
    width: 1200px;
    height: 716px;
    overflow: hidden;
    background: var(--backdrop);
  }
  .stage {
    width: 1200px;
    height: 716px;
    display: flex;
    align-items: center;
    justify-content: center;
    gap: 60px;
  }
  .card {
    width: 500px;
    height: 286px;
    box-sizing: border-box;
    box-shadow: 0 14px 30px rgba(0,0,0,0.45);
    position: relative;
    font-family: 'Lato', sans-serif;
  }
  .brand {
    display: flex;
    align-items: center;
    gap: 10px;
  }
  .brand-name {
    font-weight: 700;
    letter-spacing: 0.12em;
    text-transform: uppercase;
    white-space: nowrap;
  }

  /* contact side (black) */
  .card-contact { background: var(--card-black); }
  .card-contact .brand {
    position: absolute;
    left: 32px;
    top: 36px;
  }
  .card-contact .brand-dot { width: 18px; height: 18px; }
  .card-contact .brand-name { font-size: 14px; color: var(--silver); }
  .contact {
    position: absolute;
    left: 252px;
    top: 150px;
    color: var(--ink-dim);
  }
  .contact-name {
    margin: 0;
    font-size: 22px;
    font-weight: 700;
    color: var(--ink-mid);
  }
  .contact-role { margin: 2px 0 14px; font-size: 11px; }
  .contact-phone {
    margin: 0 0 10px;
    font-size: 22px;
    color: var(--ink-mid);
  }
  .contact-email { margin: 0; font-size: 10px; }

  /* logo side (white) */
  .card-logo {
    background: var(--card-white);
    display: flex;
    flex-direction: column;
    align-items: center;
    justify-content: center;
    gap: 16px;
  }
  .card-logo .brand-dot { width: 26px; height: 26px; }
  .card-logo .brand-name { font-size: 22px; color: var(--gold); }
  .tagline {
    margin: 0;
    font-size: 12px;
    letter-spacing: 0.04em;
    color: var(--ink-dark);
  }
</style>
</head>
<body>
  <main class="stage">
    <section class="card card-contact">
      <div class="brand">
        <svg class="brand-dot" viewBox="0 0 20 20" aria-hidden="true"><circle cx="10" cy="10" r="8.5" fill="none" stroke="#c9c9c9" stroke-width="2"/></svg>
        <span class="brand-name">TalvrenPro Athletics</span>
      </div>
      <div class="contact">
        <p class="contact-name">Marcus Tolley</p>
        <p class="contact-role">Owner and Trainer</p>
        <p class="contact-phone">555.273.8492</p>
        <p class="contact-email">marcus.tolley@talvrenproathletics.com</p>
      </div>
    </section>
    <section class="card card-logo">
      <div class="brand">
        <svg class="brand-dot" viewBox="0 0 20 20" aria-hidden="true"><circle cx="10" cy="10" r="8.5" fill="none" stroke="#b8913f" stroke-width="2"/></svg>
        <span class="brand-name">TalvrenPro Athletics</span>
      </div>
      <p class="tagline">Sports Performance and Functional Strength Training</p>
    </section>
  </main>
</body>
</html>
```